Brightwell Consulting Business Card Design

Business Card Design for Brightwell Consulting. Brightwell Consulting is a boutique consultancy based in Atlanta, GA., that specializes in marketing strategy, organization planning, and leadership development. We provide solutions for small businesses and startups as well as Summit 400 companies.

http://brightwellconsulting.example/

Target Market(s)

We provide solutions for small businesses and startups as well as Summit 400 companies.

Industry/Entity Type

Consulting

Contact Information for Business Card

Two sided business card with priority on contact information, logo, tag line (Inspiration to Dream More, Do More, Become More)

Colors

Designer to choose colors to be used in the design.

Requirements
Must have
• contact information, logo, tag line (Inspiration to Dream More, Do More, Become More)
• Simple no over communication.
Nice to have
• I would like to see different placements of logo and creative use of both sides of the card
Should not have
• Do not put too much information on the card.

```html
<!DOCTYPE html>
<html lang="en">
<head>
<meta charset="utf-8">
<title>Brightwell Consulting Business Card</title>
<link rel="stylesheet" href="https://fonts.googleapis.com/css2?family=Lato:wght@300;400;700&display=swap">
<style>
  :root {
    --canvas: #e9e7e4;
    --card-light: #ffffff;
    --card-dark: #333335;
    --corner: #2f2f31;
    --ink-dark: #2b2b2d;
    --ink-light: #f4f4f4;
    --ink-muted: #c9c9c9;
    --ink-soft: #6a6a6c;
    --pattern-a: #f7f7f7;
    --pattern-b: #eeeeee;
  }
  * { box-sizing: border-box; margin: 0; padding: 0; }
  html, body {
    width: 1200px; height: 1200px; overflow: hidden;
    background: var(--canvas);
    font-family: "Lato", Arial, sans-serif;
  }
  .sheet { position: relative; width: 1200px; height: 1200px; }
  .card {
    position: absolute; left: 180px; width: 840px; height: 480px;
    overflow: hidden; box-shadow: 0 10px 30px rgba(0,0,0,0.18);
  }
  .card--front { top: 90px; background: var(--card-light); }
  .card--back { top: 630px; background: var(--card-dark); color: var(--ink-light); }

  .front-texture {
    position: absolute; inset: 0;
    background: linear-gradient(135deg, var(--pattern-a), var(--pattern-b) 50%, var(--pattern-a));
  }
  .corner { position: absolute; }
  .corner--top-left { top: 0; left: 0; }
  .corner--bottom-right { bottom: 0; right: 0; }

  .wordmark {
    position: absolute; font-weight: 400; white-space: nowrap; line-height: 1;
  }
  .wordmark__name { display: block; letter-spacing: 1px; }
  .wordmark__sub { display: block; text-transform: uppercase; text-align: right; }

  .card--front .wordmark {
    left: 50%; top: 168px; transform: translateX(-50%);
    color: var(--ink-dark);
  }
  .card--front .wordmark__name { font-size: 76px; }
  .card--front .wordmark__sub { font-size: 22px; letter-spacing: 7px; margin-top: 10px; }

  .tagline {
    position: absolute; left: 0; right: 0; top: 330px; text-align: center;
    font-size: 17px; font-weight: 300; letter-spacing: 1.5px; color: var(--ink-soft);
  }

  .card--back .wordmark { left: 60px; top: 56px; color: var(--ink-light); }
  .card--back .wordmark__name { font-size: 60px; }
  .card--back .wordmark__sub { font-size: 18px; letter-spacing: 6px; margin-top: 8px; }

  .contact-list { position: absolute; list-style: none; }
  .contact-list--left { left: 60px; top: 200px; }
  .contact-list--right { right: 60px; bottom: 40px; }
  .contact-item {
    display: flex; align-items: flex-start; gap: 12px;
    font-size: 19px; line-height: 26px; font-weight: 300; color: var(--ink-light);
    margin-bottom: 6px;
  }
  .contact-list--right .contact-item { justify-content: flex-end; }
  .icon { width: 22px; height: 22px; flex: none; margin-top: 2px; }

  .person { position: absolute; right: 60px; top: 270px; text-align: right; }
  .person__name { font-size: 34px; font-weight: 400; letter-spacing: 0.5px; }
  .person__title { font-size: 16px; font-weight: 300; color: var(--ink-muted); margin-top: 4px; }
</style>
</head>
<body>
<main class="sheet">

  <section class="card card--front" aria-label="Card front">
    <div class="front-texture" role="img" aria-label="Faint repeated company name pattern"></div>
    <svg class="corner corner--top-left" width="190" height="130" viewBox="0 0 190 130">
      <polygon points="0,0 190,0 0,130" fill="var(--corner)"/>
    </svg>
    <svg class="corner corner--bottom-right" width="150" height="110" viewBox="0 0 150 110">
      <polygon points="150,0 150,110 0,110" fill="var(--corner)"/>
    </svg>
    <div class="wordmark">
      <span class="wordmark__name">Brightwell</span>
      <span class="wordmark__sub">Consulting</span>
    </div>
    <p class="tagline">Inspiration to Dream More, Do More, Become More</p>
  </section>

  <section class="card card--back" aria-label="Card back">
    <div class="wordmark">
      <span class="wordmark__name">Brightwell</span>
      <span class="wordmark__sub">Consulting</span>
    </div>

    <ul class="contact-list contact-list--left">
      <li class="contact-item">
        <svg class="icon" viewBox="0 0 24 24"><circle cx="12" cy="12" r="11" fill="var(--ink-light)"/><path d="M12 5a4 4 0 0 0-4 4c0 3 4 8 4 8s4-5 4-8a4 4 0 0 0-4-4z" fill="var(--card-dark)"/><circle cx="12" cy="9" r="1.5" fill="var(--ink-light)"/></svg>
        <span>1457 Larkspur Lane<br>Riverton, GA 30001</span>
      </li>
      <li class="contact-item">
        <svg class="icon" viewBox="0 0 24 24"><circle cx="12" cy="12" r="11" fill="var(--ink-light)"/><path d="M9 6c-1 0-2 1-2 2 0 5 4 9 9 9 1 0 2-1 2-2l-2.5-2-1.5 1c-1.5-.7-2.8-2-3.5-3.5l1-1.5z" fill="var(--card-dark)"/></svg>
        <span>555-014-2398</span>
      </li>
    </ul>

    <div class="person">
      <div class="person__name">Dorian K. Whitfield</div>
      <div class="person__title">General Manager</div>
    </div>

    <ul class="contact-list contact-list--right">
      <li class="contact-item">
        <svg class="icon" viewBox="0 0 24 24"><circle cx="12" cy="12" r="11" fill="var(--ink-light)"/><circle cx="12" cy="12" r="6" fill="none" stroke="var(--card-dark)" stroke-width="1.4"/><path d="M6 12h12M12 6c-2.5 3-2.5 9 0 12M12 6c2.5 3 2.5 9 0 12" fill="none" stroke="var(--card-dark)" stroke-width="1.2"/></svg>
        <span>brightwellconsulting.example</span>
      </li>
      <li class="contact-item">
        <svg class="icon" viewBox="0 0 24 24"><circle cx="12" cy="12" r="11" fill="var(--ink-light)"/><rect x="6" y="8" width="12" height="8" fill="none" stroke="var(--card-dark)" stroke-width="1.4"/><path d="M6 8l6 5 6-5" fill="none" stroke="var(--card-dark)" stroke-width="1.4"/></svg>
        <span>dorian@brightwellconsulting.example</span>
      </li>
    </ul>
  </section>

</main>
</body>
</html>
```